Surface Protection company needs cards

We are a New Zealand company that will apply nanotechnology coatings on surfaces to prevent growth and spread of bacteria, viruses, mold etc with a sprayer. We deal with large corporates, airlines, hospitals and schools so we are after a new modern, simple and clean look that will have great visual impact.
We a company that is focused on prevention and protection.

Company name, Vela Shield

Subtext, Antimicrobial Surface Protection

Logo, VS

Target Market(s)

Hospitals, Transport agencies, Airlines, Corporate entities

Contact Information for Business Card

Company name, VelaShield
Logo, VS

Gareth Tolley
velashieldnz@postbox.example
+64219305562
www.velashield.example.nz

Requirements
Must have
• Simple clean look.
Nice to have
• We apply nano coatings so try and incorporate this into a theme somehow

```html
<!DOCTYPE html>
<html lang="en">
<head>
<meta charset="utf-8">
<title>Vela Shield – Business Cards</title>
<link href="https://fonts.googleapis.com/css2?family=Open+Sans:wght@400;600;700&display=swap" rel="stylesheet">
<style>
  :root {
    --backdrop: #d9d9db;
    --card-white: #ffffff;
    --charcoal: #302c2e;
    --leaf-green: #72b34a;
    --lime-green: #8cc63f;
    --sky-blue: #2fb0e6;
    --teal: #74c4a6;
    --ink: #111111;
  }
  html, body {
    margin: 0;
    padding: 0;
    width: 1200px;
    height: 900px;
    overflow: hidden;
    background: var(--backdrop);
    font-family: "Open Sans", Arial, sans-serif;
  }
  .canvas {
    position: relative;
    width: 1200px;
    height: 900px;
  }
  .card {
    position: absolute;
    width: 520px;
    height: 300px;
    border-radius: 16px;
    overflow: hidden;
    box-shadow: 0 10px 24px rgba(0,0,0,0.22);
  }
  .card-front {
    left: 90px;
    top: 110px;
    background: var(--card-white);
  }
  .card-back {
    left: 590px;
    top: 480px;
    background: linear-gradient(100deg, var(--leaf-green) 0%, var(--leaf-green) 18%, var(--teal) 45%, #52b0c0 65%, var(--sky-blue) 100%);
  }
  .front-waves {
    position: absolute;
    inset: 0;
    width: 520px;
    height: 300px;
  }
  .front-brand {
    position: absolute;
    right: 50px;
    top: 48px;
    display: flex;
    align-items: center;
    gap: 12px;
    font-size: 32px;
    font-weight: 400;
    color: var(--sky-blue);
    letter-spacing: 0.5px;
  }
  .brand-dot {
    width: 13px;
    height: 13px;
    border-radius: 50%;
    background: var(--leaf-green);
  }
  .front-details {
    position: absolute;
    left: 46px;
    top: 112px;
    color: var(--leaf-green);
  }
  .holder-name {
    margin: 0;
    font-size: 18px;
    font-weight: 700;
    line-height: 1.2;
  }
  .holder-title {
    margin: 0 0 12px;
    font-size: 13px;
    line-height: 1.3;
    color: var(--sky-blue);
  }
  .tagline {
    margin: 0 0 12px;
    font-size: 14px;
    font-weight: 700;
    line-height: 1.2;
  }
  .contact-list {
    list-style: none;
    margin: 0;
    padding: 0;
    font-size: 13px;
    line-height: 1.3;
    color: var(--sky-blue);
  }
  .contact-list li {
    display: flex;
    align-items: center;
    gap: 8px;
    margin-bottom: 4px;
  }
  .contact-icon {
    width: 18px;
    height: 18px;
    flex: none;
  }
  .back-brand {
    position: absolute;
    inset: 0;
    display: flex;
    align-items: center;
    justify-content: center;
    font-size: 60px;
    font-weight: 400;
    color: var(--ink);
    letter-spacing: 1px;
  }
</style>
</head>
<body>
<main class="canvas">

  <section class="card card-front" aria-label="Business card front">
    <svg class="front-waves" viewBox="0 0 520 300" aria-hidden="true">
      <path class="swoosh-green" d="M0,82 C110,36 250,40 300,135 L0,300 Z" fill="var(--lime-green)"/>
      <path class="swoosh-blue" d="M318,78 C390,98 432,180 452,300 L416,300 C398,200 370,122 318,78 Z" fill="var(--sky-blue)"/>
      <path class="dark-panel" d="M0,100 C120,55 300,60 405,300 L0,300 Z" fill="var(--charcoal)" stroke="var(--card-white)" stroke-width="5"/>
    </svg>

    <div class="front-brand">
      <span class="brand-dot"></span>
      <span class="brand-name">Vela Shield</span>
    </div>

    <div class="front-details">
      <p class="holder-name">Gareth Tolley</p>
      <p class="holder-title">Managing Director</p>
      <p class="tagline">Antimicrobial Surface<br>Protection</p>
      <ul class="contact-list">
        <li>
          <svg class="contact-icon" viewBox="0 0 18 18" aria-hidden="true">
            <circle cx="9" cy="9" r="8" fill="none" stroke="var(--lime-green)" stroke-width="1.4"/>
            <path d="M6,5 L7.5,5 L8.2,7 L7.3,7.8 Q8,9.6 9.9,10.6 L10.7,9.7 L12.6,10.4 L12.6,12 Q9,12.6 6.7,9.6 Q5.4,7.6 6,5 Z" fill="var(--lime-green)"/>
          </svg>
          <span>+64219305562</span>
        </li>
        <li>
          <svg class="contact-icon" viewBox="0 0 18 18" aria-hidden="true">
            <circle cx="9" cy="9" r="8" fill="none" stroke="var(--lime-green)" stroke-width="1.4"/>
            <rect x="4.5" y="6" width="9" height="6.5" fill="var(--lime-green)"/>
            <path d="M4.5,6 L9,9.5 L13.5,6" fill="none" stroke="var(--charcoal)" stroke-width="1"/>
          </svg>
          <span>velashieldnz@postbox.example</span>
        </li>
        <li>
          <svg class="contact-icon" viewBox="0 0 18 18" aria-hidden="true">
            <circle cx="9" cy="9" r="8" fill="none" stroke="var(--lime-green)" stroke-width="1.4"/>
            <circle cx="9" cy="9" r="4.8" fill="none" stroke="var(--lime-green)" stroke-width="1"/>
            <ellipse cx="9" cy="9" rx="2" ry="4.8" fill="none" stroke="var(--lime-green)" stroke-width="1"/>
            <line x1="4.2" y1="9" x2="13.8" y2="9" stroke="var(--lime-green)" stroke-width="1"/>
          </svg>
          <span>www.velashield.example.nz</span>
        </li>
      </ul>
    </div>
  </section>

  <section class="card card-back" aria-label="Business card back">
    <div class="back-brand">Vela Shield</div>
  </section>

</main>
</body>
</html>
```